App für weniger Konsum
Zielgruppe
Wir sind ein Startup, das Nutzer:innen in einem bewussteren Kaufverhalten stärkt. Dabei werden Nutzer:innen psychologischen Kaufprofilen zugeordnet und individuell auf dem Weg begleitet, weniger einzukaufen. Das stärkt die Finanzen und schützt die Umwelt.
Aufgabenstellung
Das Design sollte einerseits minimalismusorientierte Nutzer:innen ansprechen (clean, ruhig), aber auch Nutzer:innen ansprechen, die sich noch nicht mit weniger / besserem Konsum beschäftigt haben.
Es wäre toll folgende Slides zu haben:
- Anmeldung / Registrierung
- Quiz (Es soll direkt zu Beginn ein Quiz aus mehreren Slides geben, das Nutzer:innen einem Kauftypen zuordnet(
- Quizergebnis (Du bist Kauftyp XYZ...)
- Home-Screen der App / Navigation
- Statistiken: Du hast diesen Monat so viel gespart...
- Slide mit Einstellungen
- 'Challenge' Slide: 10 tage aussortieren

```html
<!DOCTYPE html>
<html lang="de">
<head>
<meta charset="utf-8">
<title>Bewusst kaufen – App Screens</title>
<link rel="stylesheet" href="https://fonts.googleapis.com/css2?family=Inter:wght@400;500;600;700&display=swap">
<style>
  :root{
    --canvas:#f3f3f3;
    --white:#ffffff;
    --ink:#141414;
    --muted:#7a7a7a;
    --faint:#a8a8a8;
    --line:#e7e7e7;
    --soft:#f6f6f6;
    --lime:#c3f15e;
    --lime-soft:#eefbd4;
    --green:#6aaa10;
    --red:#e0352b;
    --violet:#8b6cf0;
    --orange:#f08a3c;
    --blue:#5a7cf0;
  }
  *{box-sizing:border-box;margin:0;padding:0}
  html,body{width:1200px;height:3187px;overflow:hidden;background:var(--canvas)}
  body{font-family:"Inter",sans-serif;color:var(--ink)}
  .board{position:absolute;left:0;top:0;width:970px;height:2576px;transform:scale(1.2371);transform-origin:0 0}
  .label{position:absolute;width:280px;text-align:center;font-size:8px;letter-spacing:.08em;color:var(--faint);text-transform:uppercase}
  .phone{position:absolute;width:280px;height:568px;border-radius:34px;background:var(--white);border:1px solid #ececec;box-shadow:0 8px 22px rgba(0,0,0,.07);overflow:hidden}
  .a{position:absolute}
  .center{left:0;right:0;text-align:center}
  .icon{width:14px;height:14px;stroke:currentColor;fill:none;stroke-width:1.6;stroke-linecap:round;stroke-linejoin:round}
  .pill-btn{position:absolute;display:flex;align-items:center;justify-content:center;border-radius:20px;font-size:11px;font-weight:500}
  .outline{border:1px solid var(--line);background:var(--white);color:var(--ink)}
  .dark{background:var(--ink);color:var(--white)}
  .lime{background:var(--lime);color:var(--ink)}
  .eyebrow{font-size:8px;font-weight:600;letter-spacing:.1em;color:var(--green);text-transform:uppercase}
  .option{position:absolute;left:27px;width:225px;border:1px solid var(--line);border-radius:14px;padding:16px 16px 0}
  .option h4{font-size:12px;font-weight:500}
  .option p{font-size:9px;color:var(--muted);margin-top:7px;line-height:13.5px;padding-right:20px}
  .option svg{position:absolute;right:15px;top:16px;color:#9a9a9a}
  .next{position:absolute;width:38px;height:38px;border-radius:50%;background:var(--lime);display:flex;align-items:center;justify-content:center;box-shadow:0 4px 12px rgba(163,220,60,.45)}
  .photo{position:absolute;overflow:hidden}
  .info-card{position:absolute;left:28px;width:225px;border-radius:14px;background:var(--soft);padding:18px 17px}
  .info-card h4{font-size:11px;font-weight:600;margin-top:12px}
  .info-card p{font-size:9px;color:var(--muted);line-height:15.5px;margin-top:6px}
  .dot-icon{width:24px;height:24px;border-radius:50%;display:flex;align-items:center;justify-content:center}
  .tabbar{position:absolute;left:0;right:0;top:500px;height:68px;background:var(--white);border-top:1px solid #f1f1f1}
  .tab{position:absolute;top:10px;width:60px;margin-left:-30px;text-align:center;font-size:7px;color:var(--faint)}
  .tab svg{width:16px;height:16px;display:block;margin:0 auto 5px;stroke:currentColor;fill:none;stroke-width:1.5;stroke-linecap:round;stroke-linejoin:round}
  .tab.active{color:var(--green);font-weight:600}
  .stat-card{position:absolute;top:334px;width:106px;height:108px;border:1px solid var(--line);border-radius:14px;padding:14px}
  .stat-card b{display:block;font-size:16px;font-weight:600;margin-top:14px}
  .stat-card span{display:block;font-size:8px;color:var(--muted);margin-top:3px;line-height:11px}
  .highlight{position:absolute;left:27px;width:226px;height:68px;border-radius:12px;background:var(--soft);padding:12px 12px 0 49px}
  .highlight .dot-icon{position:absolute;left:13px;top:13px}
  .highlight h4{font-size:10px;font-weight:600}
  .highlight p{font-size:8.5px;color:var(--muted);line-height:13px;margin-top:4px}
  .section{position:absolute;left:29px;font-size:8px;letter-spacing:.1em;color:var(--muted);text-transform:uppercase}
  .group{position:absolute;left:27px;width:225px;border:1px solid var(--line);border-radius:8px;overflow:hidden}
  .row{height:38px;display:flex;align-items:center;justify-content:space-between;padding:0 11px;font-size:10.5px;font-weight:500;border-bottom:1px solid var(--line)}
  .row:last-child{border-bottom:none}
  .row small{font-size:9px;color:var(--muted);font-weight:400}
  .row svg{width:11px;height:11px;color:#999}
  .toggle{width:30px;height:16px;border-radius:8px;background:var(--lime);position:relative}
  .toggle::after{content:"";position:absolute;right:2px;top:2px;width:12px;height:12px;border-radius:50%;background:var(--white)}
  .menu-tile{position:absolute;top:332px;width:62px;margin-left:-31px;text-align:center;font-size:8px;color:var(--muted)}
  .menu-tile i{display:flex;width:36px;height:36px;margin:0 auto 10px;border:1px solid var(--line);border-radius:50%;align-items:center;justify-content:center;color:var(--ink)}
  .menu-row{position:absolute;left:32px;right:32px;display:flex;align-items:center;font-size:11px;font-weight:500}
  .menu-row svg:first-child{margin-right:9px;color:#555}
  .menu-row .chev{margin-left:auto;width:10px;height:10px;color:#aaa}
  .divider-label{position:absolute;left:27px;width:225px;top:327px;display:flex;align-items:center;gap:8px;font-size:7.5px;letter-spacing:.1em;color:var(--faint);line-height:10px}
  .divider-label::before,.divider-label::after{content:"";flex:1;height:1px;background:var(--line)}
</style>
</head>
<body>
<svg width="0" height="0" style="position:absolute">
  <defs>
    <symbol id="i-arrow" viewBox="0 0 24 24"><path d="M5 12h14M13 6l6 6-6 6"/></symbol>
    <symbol id="i-back" viewBox="0 0 24 24"><path d="M19 12H5M11 6l-6 6 6 6"/></symbol>
    <symbol id="i-chev" viewBox="0 0 24 24"><path d="M9 6l6 6-6 6"/></symbol>
    <symbol id="i-home" viewBox="0 0 24 24"><path d="M4 10l8-6 8 6v10H4z"/><path d="M10 20v-6h4v6"/></symbol>
    <symbol id="i-stat" viewBox="0 0 24 24"><path d="M6 20v-6M12 20V5M18 20v-9"/></symbol>
    <symbol id="i-layers" viewBox="0 0 24 24"><path d="M12 4l9 5-9 5-9-5z"/><path d="M3 14l9 5 9-5"/></symbol>
    <symbol id="i-dots" viewBox="0 0 24 24"><circle cx="5" cy="12" r="1.2"/><circle cx="12" cy="12" r="1.2"/><circle cx="19" cy="12" r="1.2"/></symbol>
    <symbol id="i-clock" viewBox="0 0 24 24"><circle cx="12" cy="12" r="9"/><path d="M12 7v5l3 2"/></symbol>
    <symbol id="i-shield" viewBox="0 0 24 24"><path d="M12 3l8 3v6c0 5-4 8-8 9-4-1-8-4-8-9V6z"/></symbol>
  </defs>
</svg>

<main class="board">

  <!-- Row 1 -->
  <div class="label" style="left:33px;top:33px">1. Login &amp; Registrierung</div>
  <div class="label" style="left:345px;top:33px">2. Quiz Intro</div>
  <div class="label" style="left:657px;top:33px">3. Quiz Question 1</div>

  <section class="phone" style="left:33px;top:55px">
    <div class="a" role="img" aria-label="Platz für das App-Zeichen" style="left:120px;top:49px;width:38px;height:38px;border:1px solid var(--line);border-radius:10px"></div>
    <h1 class="a center" style="top:136px;font-size:20px;font-weight:600">Willkommen zurück</h1>
    <p class="a center" style="top:170px;font-size:10.5px;color:var(--muted)">Dein Begleiter für bewusstes Konsumieren.</p>
    <div class="pill-btn outline" style="left:27px;top:212px;width:225px;height:37px">Mit Ferolia anmelden</div>
    <div class="pill-btn outline" style="left:27px;top:258px;width:225px;height:37px">Mit Quintaro anmelden</div>
    <div class="divider-label">ODER MIT EMAIL</div>
    <p class="a" style="left:37px;top:371px;font-size:7.5px;color:#555">Email Adresse</p>
    <div class="a" style="left:27px;top:387px;width:225px;height:37px;background:var(--soft);border-radius:10px;padding:12px 15px;font-size:10.5px;color:var(--faint)">name@beispiel.de</div>
    <div class="pill-btn lime" style="left:27px;top:441px;width:225px;height:37px;font-weight:600">Weiter</div>
    <p class="a center" style="top:530px;font-size:7px;color:var(--faint)">Mit der Anmeldung akzeptierst du unsere <u>AGB</u> .</p>
  </section>

  <section class="phone" style="left:345px;top:55px">
    <div class="a" style="left:27px;top:37px;width:26px;height:26px;border:1px solid var(--line);border-radius:50%;display:flex;align-items:center;justify-content:center">
      <svg class="icon" style="width:10px;height:10px" viewBox="0 0 24 24"><path d="M6 6l12 12M18 6L6 18"/></svg>
    </div>
    <div class="a" style="left:38px;top:75px;width:204px;height:170px;border-radius:16px;background:var(--white);box-shadow:0 6px 18px rgba(0,0,0,.08)"></div>
    <div class="photo" role="img" aria-label="Foto: Hand greift nach Kleidung auf einer Kleiderstange" style="left:52px;top:85px;width:181px;height:145px;background:linear-gradient(100deg,#2a2a2a 0%,#d9d6d0 30%,#3b3b3b 50%,#8c8881 75%,#1f1f1f 100%)"></div>
    <h2 class="a center" style="top:274px;font-size:22px;font-weight:500;line-height:25px">Lerne deinen<br>Kaufstil kennen</h2>
    <p class="a center" style="top:332px;font-size:12.5px;line-height:20px;color:var(--muted)">Dieses kurze Quiz hilft uns zu<br>verstehen, was deine<br>Kaufentscheidungen antreibt.</p>
    <div class="a" style="left:38px;top:418px;width:204px;height:68px;background:var(--soft);border-radius:12px;padding:15px 16px;font-size:9px;color:#444;line-height:22px">
      <div style="display:flex;align-items:center;gap:7px"><svg class="icon" style="width:11px;height:11px;color:var(--green)"><use href="#i-clock"/></svg>Dauer: ca. 2 Minuten</div>
      <div style="display:flex;align-items:center;gap:7px"><svg class="icon" style="width:11px;height:11px;color:var(--green)"><use href="#i-shield"/></svg>Daten bleiben privat</div>
    </div>
    <div class="pill-btn dark" style="left:27px;top:497px;width:226px;height:43px;justify-content:space-between;padding:0 22px;border-radius:22px">Starten<svg class="icon" style="width:12px;height:12px"><use href="#i-arrow"/></svg></div>
  </section>

  <section class="phone" style="left:657px;top:55px">
    <div class="a" style="left:20px;top:4px;width:240px;height:4px;border-radius:2px;background:#f0f0f0"><div style="width:40px;height:4px;border-radius:2px;background:var(--lime)"></div></div>
    <p class="a eyebrow" style="left:27px;top:48px">Situation 01/05</p>
    <h3 class="a" style="left:27px;top:66px;font-size:16px;font-weight:400;line-height:22px">Du betrittst ein Geschäft.<br>Wohin geht dein erster Blick?</h3>
    <div class="option" style="top:198px;height:69px"><h4>Zur Sale-Abteilung</h4><p>Ich liebe es, Schnäppchen zu finden.</p>
      <svg class="icon" style="width:12px;height:12px" viewBox="0 0 24 24"><path d="M19 5L5 19"/><circle cx="7" cy="7" r="2"/><circle cx="17" cy="17" r="2"/></svg></div>
    <div class="option" style="top:280px;height:69px"><h4>Zu den Neuheiten</h4><p>Ich möchte wissen, was im Trend liegt.</p>
      <svg class="icon" style="width:12px;height:12px" viewBox="0 0 24 24"><path d="M10 4l2 6 6 2-6 2-2 6-2-6-6-2 6-2z"/><path d="M19 3v4M17 5h4"/></svg></div>
    <div class="option" style="top:362px;height:69px"><h4>Gezielt zum Produkt</h4><p>Ich hole nur, was ich brauche.</p>
      <svg class="icon" style="width:12px;height:12px" viewBox="0 0 24 24"><circle cx="12" cy="12" r="9"/><circle cx="12" cy="12" r="5"/><circle cx="12" cy="12" r="1"/></svg></div>
    <div class="next" style="left:216px;top:502px"><svg class="icon"><use href="#i-arrow"/></svg></div>
  </section>

  <!-- Row 2 -->
  <div class="label" style="left:33px;top:656px">4. Quiz Question 2</div>
  <div class="label" style="left:345px;top:656px">8. Quiz Result</div>
  <div class="label" style="left:657px;top:656px">9. Profile Detail</div>

  <section class="phone" style="left:33px;top:677px">
    <div class="a" style="left:19px;top:4px;width:240px;height:4px;border-radius:2px;background:#f0f0f0"><div style="width:93px;height:4px;border-radius:2px;background:var(--lime)"></div></div>
    <p class="a eyebrow" style="left:27px;top:48px">Situation 02/05</p>
    <h3 class="a" style="left:27px;top:66px;font-size:16px;font-weight:400;line-height:22px">Ein stressiger Tag geht zu<br>Ende. Du siehst eine Werbung.<br>Was fühlst du?</h3>
    <div class="option" style="top:189px;height:83px"><h4>Belohnung</h4><p>Der Kauf würde mir sofort gute Laune machen.</p>
      <svg class="icon" style="width:12px;height:12px" viewBox="0 0 24 24"><rect x="4" y="9" width="16" height="11"/><path d="M3 9h18M12 9v11M12 9c-2-4-6-4-6-1s6 1 6 1 6 2 6-1-4-3-6 1"/></svg></div>
    <div class="option" style="top:285px;height:83px"><h4>Gleichgültigkeit</h4><p>Ich scrolle weiter, es berührt mich heute nicht.</p>
      <svg class="icon" style="width:12px;height:12px" viewBox="0 0 24 24"><circle cx="12" cy="12" r="9"/><path d="M8 15h8M9 10h.01M15 10h.01"/></svg></div>
    <div class="option" style="top:380px;height:83px"><h4>Kaufdruck</h4><p>Ich habe Angst, ein gutes Angebot zu verpassen.</p>
      <svg class="icon" style="width:12px;height:12px" viewBox="0 0 24 24"><circle cx="12" cy="12" r="9"/><path d="M12 7v6M12 16.5v.5"/></svg></div>
    <div class="next" style="left:215px;top:503px"><svg class="icon"><use href="#i-arrow"/></svg></div>
  </section>

  <section class="phone" style="left:345px;top:677px">
    <div class="a" style="left:6px;top:250px;right:6px;bottom:6px;border-radius:0 0 30px 30px;background:linear-gradient(180deg,rgba(238,251,212,0) 0%,#f2fbdf 70%,#eaf9cd 100%)"></div>
    <div class="photo" role="img" aria-label="Foto: nebliger Nadelwald" style="left:78px;top:104px;width:124px;height:124px;border-radius:50%;border:3px solid var(--white);box-shadow:0 6px 16px rgba(0,0,0,.12);background:linear-gradient(180deg,#c9cfcc 0%,#7c8c84 40%,#2f4a38 75%,#1e3325 100%)"></div>
    <div class="a" style="left:118px;top:144px;width:44px;height:44px;border-radius:50%;background:rgba(255,255,255,.92);display:flex;align-items:center;justify-content:center">
      <svg class="icon" style="width:18px;height:18px;color:var(--green);stroke-width:2" viewBox="0 0 24 24"><path d="M12 20s-8-5-8-11a4 4 0 0 1 8-1 4 4 0 0 1 8 1c0 6-8 11-8 11z"/><path d="M8 12h3l1-2 1 4 1-2h2"/></svg>
    </div>
    <p class="a center eyebrow" style="top:254px;font-size:8.5px">Dein Ergebnis</p>
    <h2 class="a center" style="top:276px;font-size:24px;font-weight:600;line-height:27px">Der emotionale<br>Ausgleicher</h2>
    <p class="a center" style="top:342px;font-size:12px;line-height:20px;color:var(--muted)">Du nutzt Einkäufe oft unbewusst, um<br>für Balance in stressigen Zeiten zu<br>sorgen.</p>
    <div class="pill-btn dark" style="left:74px;top:428px;width:132px;height:37px;gap:6px">Mehr erfahren<svg class="icon" style="width:9px;height:9px" viewBox="0 0 24 24"><path d="M6 9l6 6 6-6"/></svg></div>
  </section>

  <section class="phone" style="left:657px;top:677px">
    <div class="a" style="left:28px;top:38px;width:26px;height:26px;border:1px solid var(--line);border-radius:50%;display:flex;align-items:center;justify-content:center"><svg class="icon" style="width:12px;height:12px"><use href="#i-back"/></svg></div>
    <p class="a" style="left:65px;top:44px;font-size:12.5px;font-weight:500">Dein Profil</p>
    <h2 class="a" style="left:28px;top:87px;font-size:20px;font-weight:600;line-height:24px">Der emotionale<br>Ausgleicher</h2>
    <div class="info-card" style="top:155px;height:141px">
      <div class="dot-icon" style="background:#e9edff;color:var(--blue)"><svg class="icon" style="width:12px;height:12px" viewBox="0 0 24 24"><path d="M13 3L5 14h6l-1 7 8-11h-6z"/></svg></div>
      <h4>Der Auslöser</h4>
      <p>Oft ist es nicht das Produkt selbst, sondern das Gefühl des "Sich-Gönnens" nach Anstrengung oder Stress.</p>
    </div>
    <div class="info-card" style="top:313px;height:141px">
      <div class="dot-icon" style="background:#fff0e3;color:var(--orange)"><svg class="icon" style="width:12px;height:12px" viewBox="0 0 24 24"><path d="M12 4l9 16H3z"/><path d="M12 10v4M12 17v.5"/></svg></div>
      <h4>Die Falle</h4>
      <p>Kurzfristige Freude verwandelt sich schnell in Gleichgültigkeit gegenüber dem Gegenstand.</p>
    </div>
    <div class="a" style="left:28px;top:470px;width:225px;height:26px;border-radius:14px 14px 0 0;background:linear-gradient(180deg,var(--lime-soft),rgba(255,255,255,0))"></div>
    <div class="a" style="left:0;right:0;top:478px;height:90px;background:linear-gradient(180deg,rgba(255,255,255,0),#fff 30%)"></div>
    <div class="pill-btn dark" style="left:28px;top:503px;width:225px;height:37px">Mein Dashboard öffnen</div>
  </section>

  <!-- Row 3 -->
  <div class="label" style="left:33px;top:1278px">10. Home Dashboard</div>
  <div class="label" style="left:345px;top:1278px">11. Statistics</div>
  <div class="label" style="left:657px;top:1278px">12. Challenge Details</div>

  <section class="phone" style="left:33px;top:1299px">
    <p class="a" style="left:27px;top:38px;font-size:9px;color:#555">Dienstag, 24. Okt</p>
    <h3 class="a" style="left:27px;top:55px;font-size:16px;font-weight:600">Guten Morgen, Anna</h3>
    <div class="photo" role="img" aria-label="Profilbild von Anna" style="left:221px;top:44px;width:30px;height:30px;border-radius:50%;border:2px solid var(--white);box-shadow:0 2px 6px rgba(0,0,0,.2);background:linear-gradient(135deg,#8a6a55,#3a2a22)"></div>
    <div class="photo" role="img" aria-label="Foto: Person mit ausgebreiteten Armen am Meer bei Sonnenuntergang" style="left:27px;top:97px;width:225px;height:214px;border-radius:22px;background:linear-gradient(180deg,#3a4a55 0%,#7a4a3a 40%,#c9583a 55%,#3a3030 75%,#1b1c20 100%)">
      <span class="a" style="left:20px;top:23px;padding:4px 8px;border-radius:10px;background:rgba(255,255,255,.22);font-size:6.5px;letter-spacing:.08em;color:var(--white);font-weight:600">DAILY INSIGHT</span>
      <p class="a" style="left:21px;top:123px;font-size:17px;line-height:24px;color:var(--white)">"Nicht zu kaufen ist<br>auch eine Einnahme."</p>
      <p class="a" style="left:21px;top:181px;font-size:8.5px;color:rgba(255,255,255,.9);display:flex;align-items:center;gap:5px">Gedanken notieren <svg class="icon" style="width:9px;height:9px"><use href="#i-arrow"/></svg></p>
    </div>
    <div class="stat-card" style="left:27px">
      <div class="dot-icon" style="background:var(--lime-soft);color:var(--green)"><svg class="icon" style="width:11px;height:11px" viewBox="0 0 24 24"><path d="M5 11c0-4 4-6 8-6 4 0 6 2 7 4h1v4h-2l-2 3v3h-3v-2H10v2H7v-3c-1-1-2-3-2-5z"/></svg></div>
      <b>42€</b><span>Diese Woche<br>gespart</span>
    </div>
    <div class="stat-card" style="left:146px">
      <div class="dot-icon" style="background:#fff0e3;color:var(--orange)"><svg class="icon" style="width:11px;height:11px" viewBox="0 0 24 24"><path d="M3 12h4l3-7 4 14 3-7h4"/></svg></div>
      <b>3</b><span>Impulse vermieden</span>
    </div>
    <h4 class="a" style="left:27px;top:466px;font-size:12px;font-weight:600">Aktive Challenge</h4>
    <nav class="tabbar">
      <div class="tab active" style="left:48px"><span class="a" style="left:10px;top:-4px;width:40px;height:40px;border-radius:50%;background:radial-gradient(circle,rgba(195,241,94,.35),rgba(195,241,94,0) 70%)"></span><svg style="fill:var(--green);position:relative"><use href="#i-home"/></svg><span style="position:relative">Home</span></div>
      <div class="tab" style="left:106px"><svg><use href="#i-stat"/></svg>Statistik</div>
      <div class="tab" style="left:170px"><svg><use href="#i-layers"/></svg>Challenge</div>
      <div class="tab" style="left:231px"><svg><use href="#i-dots"/></svg>Menü</div>
    </nav>
  </section>

  <section class="phone" style="left:345px;top:1299px">
    <h3 class="a" style="left:27px;top:38px;font-size:16px;font-weight:500">Deine Erfolge</h3>
    <span class="a" style="left:205px;top:40px;width:48px;height:16px;border:1px solid var(--line);border-radius:8px;font-size:7.5px;color:#555;text-align:center;line-height:14px">Oktober</span>
    <p class="a center" style="top:104px;font-size:9px;color:#555">Gespart durch Bewusstsein</p>
    <p class="a center" style="top:116px;font-size:32px;font-weight:600;letter-spacing:-.01em">245€</p>
    <p class="a center" style="top:160px;font-size:8.5px;color:var(--green);font-weight:500">↗ +120€ zum Vormonat</p>
    <div class="a" style="left:37px;top:274px;width:44px;height:22px;background:#f0f0f0"></div>
    <div class="a" style="left:91px;top:252px;width:44px;height:44px;background:#f0f0f0"></div>
    <div class="a" style="left:145px;top:263px;width:44px;height:33px;background:#f0f0f0"></div>
    <div class="a" style="left:199px;top:220px;width:44px;height:76px;background:#a8e83a"></div>
    <span class="a" style="left:196px;top:194px;width:50px;height:15px;background:var(--ink);border-radius:3px;color:var(--white);font-size:7px;text-align:center;line-height:15px">Woche 4</span>
    <p class="a section" style="left:27px;top:330px;font-size:8.5px">Highlights</p>
    <div class="highlight" style="top:353px">
      <div class="dot-icon" style="background:#efe9ff;color:var(--violet)"><svg class="icon" style="width:11px;height:11px" viewBox="0 0 24 24"><circle cx="12" cy="12" r="9"/><path d="M12 3v18M3 12h18"/></svg></div>
      <h4>3x "Nein" gesagt</h4><p>Du hast drei Impulskäufe in der Kategorie "Technik" vermieden.</p>
    </div>
    <div class="highlight" style="top:432px">
      <div class="dot-icon" style="background:#e6edff;color:var(--blue)"><svg class="icon" style="width:11px;height:11px"><use href="#i-clock"/></svg></div>
      <h4>24h Wartezeit eingehalten</h4><p>Bei deinem Wunschzettel hast du Geduld bewiesen.</p>
    </div>
    <nav class="tabbar">
      <div class="tab" style="left:48px"><svg><use href="#i-home"/></svg>Home</div>
      <div class="tab active" style="left:106px"><svg><use href="#i-stat"/></svg>Statistik</div>
      <div class="tab" style="left:170px"><svg><use href="#i-layers"/></svg>Challenge</div>
      <div class="tab" style="left:231px"><svg><use href="#i-dots"/></svg>Menü</div>
    </nav>
  </section>

  <section class="phone" style="left:657px;top:1299px">
    <div class="a" style="left:28px;top:38px;width:26px;height:26px;border:1px solid var(--line);border-radius:50%;display:flex;align-items:center;justify-content:center"><svg class="icon" style="width:12px;height:12px"><use href="#i-back"/></svg></div>
    <svg class="icon a" style="left:233px;top:44px;width:13px;height:13px" viewBox="0 0 24 24"><circle cx="18" cy="5" r="2.5"/><circle cx="6" cy="12" r="2.5"/><circle cx="18" cy="19" r="2.5"/><path d="M8 11l8-5M8 13l8 5"/></svg>
    <div class="photo" role="img" aria-label="Foto: Mütze, Strickpullover, Jeans und Tulpen auf weißem Grund" style="left:28px;top:86px;width:225px;height:128px;border-radius:14px;background:linear-gradient(120deg,#b85a3a 0%,#e6e2dc 35%,#9aa3ad 55%,#c8d3df 75%,#efe6b0 100%)"></div>
    <span class="a" style="left:105px;top:235px;width:72px;height:14px;border-radius:7px;background:var(--lime-soft);color:var(--green);font-size:7px;font-weight:600;letter-spacing:.1em;text-align:center;line-height:14px">CHALLENGE</span>
    <h2 class="a center" style="top:258px;font-size:22px;font-weight:600;line-height:24px">10 Tage<br>Aussortieren</h2>
    <p class="a center" style="top:312px;font-size:11px;line-height:16px;color:var(--muted)">Schaffe Raum für Neues, indem du Altes<br>loslässt.</p>
    <div class="a" style="left:28px;top:366px;width:225px;height:160px;border:1px solid var(--line);border-radius:14px"></div>
    <div class="a" style="left:124px;top:383px;width:32px;height:32px;border-radius:50%;background:var(--lime);font-size:12px;font-weight:600;text-align:center;line-height:32px">01</div>
    <h4 class="a center" style="top:427px;font-size:13px;font-weight:600">Der Kleiderschrank</h4>
    <p class="a center" style="top:449px;font-size:9px;line-height:15.5px;color:var(--muted)">Finde 3 Teile, die du seit einem Jahr nicht<br>getragen hast. Spende oder verkaufe sie<br>heute.</p>
    <nav class="tabbar">
      <div class="tab" style="left:48px"><svg><use href="#i-home"/></svg>Home</div>
      <div class="tab" style="left:106px"><svg><use href="#i-stat"/></svg>Statistik</div>
      <div class="tab active" style="left:170px"><svg style="fill:var(--green)"><use href="#i-layers"/></svg>Challenge</div>
      <div class="tab" style="left:231px"><svg><use href="#i-dots"/></svg>Menü</div>
    </nav>
  </section>

  <!-- Row 4 -->
  <div class="label" style="left:33px;top:1900px">13. Settings</div>
  <div class="label" style="left:345px;top:1900px">14. Menu / Navigation Drawer</div>

  <section class="phone" style="left:33px;top:1921px">
    <h2 class="a" style="left:27px;top:38px;font-size:20px;font-weight:500">Einstellungen</h2>
    <p class="section" style="top:84px">Präferenzen</p>
    <div class="group" style="top:103px">
      <div class="row">Mitteilungen<span class="toggle"></span></div>
      <div class="row">Daily Reminder Zeit<small>08:00</small></div>
    </div>
    <p class="section" style="top:202px">Account &amp; Daten</p>
    <div class="group" style="top:221px">
      <div class="row">Profil bearbeiten<svg class="icon"><use href="#i-chev"/></svg></div>
      <div class="row">Exportiere meine Daten<svg class="icon" viewBox="0 0 24 24"><path d="M12 4v11M7 10l5 5 5-5M4 20h16"/></svg></div>
      <div class="row">Privatsphäre<svg class="icon" viewBox="0 0 24 24"><rect x="5" y="11" width="14" height="9" rx="1"/><path d="M8 11V8a4 4 0 0 1 8 0v3"/></svg></div>
    </div>
    <p class="section" style="top:358px">Support</p>
    <div class="group" style="top:377px">
      <div class="row">Hilfe &amp; FAQ<svg class="icon" viewBox="0 0 24 24"><path d="M14 4h6v6M20 4l-9 9M18 14v6H4V6h6"/></svg></div>
    </div>
    <p class="a center" style="top:457px;font-size:9.5px;color:var(--red);font-weight:500">Abmelden</p>
    <p class="a center" style="top:489px;font-size:6px;color:var(--faint)">Version 1.0.2 • Build 2490</p>
    <nav class="tabbar">
      <div class="tab" style="left:48px"><svg><use href="#i-home"/></svg>Home</div>
      <div class="tab" style="left:106px"><svg><use href="#i-stat"/></svg>Statistik</div>
      <div class="tab" style="left:170px"><svg><use href="#i-layers"/></svg>Challenge</div>
      <div class="tab active" style="left:231px"><svg style="stroke-width:2.4"><use href="#i-dots"/></svg>Menü</div>
    </nav>
  </section>

  <section class="phone" style="left:345px;top:1921px">
    <div class="a" style="left:6px;top:6px;right:6px;bottom:6px;border-radius:30px;background:#d6d6d6;overflow:hidden">
      <div style="filter:blur(1.6px)">
        <p class="a" style="left:20px;top:34px;font-size:9px;color:#8a8a8a">Dienstag, 24. Okt</p>
        <p class="a" style="left:20px;top:51px;font-size:16px;font-weight:600;color:#6a6a6a">Guten Morgen, Anna</p>
        <div class="a" style="left:21px;top:91px;width:226px;height:214px;border-radius:22px;background:#c4c4c4"></div>
      </div>
      <div class="a" style="left:0;right:0;top:286px;bottom:0;background:var(--white);border-radius:28px 28px 0 0"></div>
    </div>
    <div class="a" style="left:125px;top:308px;width:30px;height:3px;border-radius:2px;background:#dcdcdc"></div>
    <div class="menu-tile" style="left:47px"><i><svg class="icon" viewBox="0 0 24 24"><circle cx="12" cy="8" r="4"/><path d="M4 20c1-4 4-6 8-6s7 2 8 6"/></svg></i>Profil</div>
    <div class="menu-tile" style="left:109px"><i><svg class="icon" viewBox="0 0 24 24"><circle cx="12" cy="12" r="3"/><path d="M12 2v3M12 19v3M2 12h3M19 12h3M4.9 4.9l2.1 2.1M17 17l2.1 2.1M4.9 19.1L7 17M17 7l2.1-2.1"/></svg></i>Einstellungen</div>
    <div class="menu-tile" style="left:171px"><i><svg class="icon" viewBox="0 0 24 24"><path d="M6 16V11a6 6 0 0 1 12 0v5l2 2H4z"/><path d="M10 20a2 2 0 0 0 4 0"/></svg></i>Mitteilungen</div>
    <div class="menu-tile" style="left:233px"><i><svg class="icon" viewBox="0 0 24 24"><circle cx="12" cy="12" r="9"/><path d="M9.5 9.5a2.5 2.5 0 0 1 5 0c0 2-2.5 2-2.5 4M12 17v.5"/></svg></i>Hilfe</div>
    <div class="menu-row" style="top:424px"><svg class="icon" style="width:12px;height:12px"><use href="#i-shield"/></svg>Datenschutz &amp; AGB<svg class="icon chev"><use href="#i-chev"/></svg></div>
    <div class="menu-row" style="top:467px"><svg class="icon" style="width:12px;height:12px" viewBox="0 0 24 24"><path d="M12 3l2.8 5.8 6.2.9-4.5 4.4 1 6.2L12 17.4 6.5 20.3l1-6.2L3 9.7l6.2-.9z"/></svg>App Bewerten<svg class="icon chev"><use href="#i-chev"/></svg></div>
    <div class="menu-row" style="top:510px;color:var(--red)"><svg class="icon" style="width:12px;height:12px;color:var(--red)" viewBox="0 0 24 24"><path d="M10 4H5v16h5M14 8l4 4-4 4M18 12H9"/></svg>Abmelden</div>
  </section>

</main>
</body>
</html>
```